Gentleman's grooming products require a business card

I need a business card that incorporates the logo [ or parts of ] that we had Art Parade design for us as uploaded.

We sell online, mens grooming products including moustache waxes, beard oils and shaving accessories.
We want a card that is classy, professional and a card that shouts mens products.

Target Market(s)

Young professional male market

Industry/Entity Type

Business

Contact Information for Business Card

Tess and Dulcie Abbott
Brass and Bristle
Purveyors of gentleman's stiffeners and grooming requisites
M :0491527306
E : tess@brassandbristle.com.au
E : dulcie@brassandbristle.com.au
E : sales@theboulevardpomade.com.au

W : www.brassandbristle.com.au

Requirements
Must have
• Class
Nice to have
• Professionalism

```html
<!DOCTYPE html>
<html lang="en">
<head>
<meta charset="utf-8">
<title>Brass and Bristle — Business Cards</title>
<link rel="stylesheet" href="https://fonts.googleapis.com/css2?family=Cinzel:wght@400;600&family=Roboto+Condensed:wght@400;700&family=Arimo:wght@400;700&display=swap">
<style>
  :root {
    --backdrop: #8c8c8c;
    --card: #000000;
    --ink: #ffffff;
  }
  * { margin: 0; padding: 0; box-sizing: border-box; }
  html, body {
    width: 1200px;
    height: 1200px;
    overflow: hidden;
    background: var(--backdrop);
  }
  .board {
    position: relative;
    width: 1200px;
    height: 1200px;
  }
  .card {
    position: absolute;
    top: 138px;
    width: 560px;
    height: 926px;
    background: var(--card);
    color: var(--ink);
    text-align: center;
  }
  .card--tess { left: 30px; }
  .card--dulcie { left: 610px; }

  .card__rule {
    position: absolute;
    left: 0;
    top: 327px;
    width: 100%;
    height: 3px;
    background: var(--ink);
  }
  .card__mark {
    position: absolute;
    left: 50%;
    top: 253px;
    width: 150px;
    height: 150px;
    margin-left: -75px;
    background: var(--card);
    border: 4px solid var(--ink);
  }
  .brand {
    position: absolute;
    left: 0;
    right: 0;
    top: 436px;
    font-family: "Cinzel", serif;
    font-weight: 400;
    font-size: 44px;
    line-height: 56px;
    letter-spacing: 1px;
  }
  .brand__rule {
    position: absolute;
    left: 50px;
    right: 50px;
    top: 505px;
    height: 3px;
    background: var(--ink);
  }
  .tagline {
    position: absolute;
    left: 0;
    right: 0;
    top: 516px;
    font-family: "Cinzel", serif;
    font-weight: 400;
    font-size: 19px;
    line-height: 26px;
    letter-spacing: 0.6px;
  }
  .person {
    position: absolute;
    left: 0;
    right: 0;
    top: 624px;
    font-family: "Roboto Condensed", sans-serif;
    font-weight: 700;
    font-size: 40px;
    line-height: 48px;
  }
  .contact {
    position: absolute;
    left: 0;
    right: 0;
    top: 730px;
    font-family: "Roboto Condensed", sans-serif;
    font-weight: 400;
    font-size: 30px;
    line-height: 40px;
  }
  .web {
    position: absolute;
    left: 0;
    right: 0;
    top: 860px;
    font-family: "Arimo", sans-serif;
    font-weight: 400;
    font-size: 25px;
    line-height: 32px;
  }
  .web b { font-weight: 700; }
</style>
</head>
<body>
<main class="board">

  <section class="card card--tess">
    <div class="card__rule"></div>
    <div class="card__mark"></div>
    <h1 class="brand">Brass and Bristle</h1>
    <div class="brand__rule"></div>
    <p class="tagline">Purveyors of Gentleman’s Stiffeners<br>and Grooming Requisites</p>
    <h2 class="person">Tess</h2>
    <p class="contact">0491527306<br>tess@brassandbristle.com.au</p>
    <p class="web">www.<b>brassandbristle</b>.com.au</p>
  </section>

  <section class="card card--dulcie">
    <div class="card__rule"></div>
    <div class="card__mark"></div>
    <h1 class="brand">Brass and Bristle</h1>
    <div class="brand__rule"></div>
    <p class="tagline">Purveyors of Gentleman’s Stiffeners<br>and Grooming Requisites</p>
    <h2 class="person">Dulcie Abbott</h2>
    <p class="contact">0491527306<br>dulcie@brassandbristle.com.au</p>
    <p class="web">www.<b>brassandbristle</b>.com.au</p>
  </section>

</main>
</body>
</html>
```